Packaging Design Required for Premium Skincare Range

We require design for packaging boxes and labels (label to be printed via silkscreen on the bottles) for our skincare products. The overall look should be streamlined for the entire range, so as to have a strong brand image.

As these products are made in Singapore, we would like to incorporate a bit of ‘batik’ element into the design of boxes. A tiny symbol of the ‘Lion Head’ should be placed next to the words ‘Made in Singapore’. Attached is a file of the ‘Lion Head’.

Look and feel:
Upmarket, premium, elegant, feminine, natural

Examples of designs we like:
www.velumira.com
https://www.quorin.com/sg/
http://bownecosmetics.com/bowne-shop-skincare

The above are 3 different design concepts. Please explore how to integrate elements of these 3 concepts to come up with something original. The final design should communicate high product efficacy, elegance, premium and natural.

Design Scope:
1. Packaging Boxes:
Colors can be used to differentiate one product from another. However, the brand name and icon should be the same color for all products. The final print ready artwork should be of the right size/proportion to contain the bottles.

2. Labels (To be printed via silkscreen on the bottles):
One single color only for each product label. The pantone color is stated in the information for each product in the attached file. The final print ready artwork should be of the right size/proportion to be printed on the bottles.

Product Range (Total 6 products):
1. Amino Acid Cleansing Mousse
(Height of printable area of bottle: 10.8cm
Height of whole bottle with cap: 17cm
Diameter: 4.7cm)

2. Revitalizing Tonic
(Height of printable area of bottle: 13.6cm
Height of whole bottle with cap: 17.5cm
Diameter: 4cm) (The actual cap for this bottle is white and
not brown in the photo)

3. Soothing Moisturizer with Antioxidants
(Height of printable area of bottle: 9cm
Height of whole bottle with cap: 16.3cm
Diameter: 2.8cm)

4. Pore Clarifying Essence
Diameter: 2.5cm)

5. Intense Whitening Serum
Diameter: 2.8cm)

6. Cell Repair Concentrate
Diameter: 2.8cm)

Attached are the various files:
1. Brand logo (pantone 2755)
2. Lion Head symbol (pantone 032)
3. Information for each product's packaging and label
4. Photos of bottles
5. Examples of batik motifs.
Please feel free to look for other batik motifs which you feel can achieve the design effect. Also, it's for the outer packaging boxes only, not for the silkscreen label. Please explore how to integrate into the design in a tasteful and elegant way, without overwhelming or clutter. Or if your design is better without the batik motifs, please feel free to suggest.

Artwork files should be:
- Print-ready editable ai, png, eps, jpg files
- Includes front, back, and sides of boxes and labels
- Include source files
- Include 3-D mock-ups

Women of all ages, beauty bloggers, people who cares about their skin and want to look good, skincare connoissuers

• Century New Gothic or similar

• A strong brand image, a brand that communicates class, product efficacy, & natural premium ingredients.
• Clutter, embossing

```html
<!DOCTYPE html>
<html lang="en">
<head>
<meta charset="utf-8">
<title>Aurelyne – Amino Acid Cleansing Mousse Labels</title>
<link rel="stylesheet" href="https://fonts.googleapis.com/css2?family=Questrial&family=Mulish:wght@700&display=swap">
<style>
  :root {
    --navy: #2b2f72;
    --ink: #3a3a3a;
    --teal: #8fd9d6;
    --teal-deep: #5cc4c0;
    --teal-soft: #e3f6f6;
    --rule: #c9c9c9;
    --paper: #ffffff;
    --stage: #e4e4e4;
    --lavender: #8b6bb8;
    --blossom: #f19a3a;
  }
  * { box-sizing: border-box; margin: 0; padding: 0; }
  html, body { width: 907px; height: 1200px; overflow: hidden; }
  body {
    background: var(--stage);
    position: relative;
    font-family: "Questrial", "Century Gothic", sans-serif;
    color: var(--ink);
  }
  .label {
    position: absolute;
    left: 98px;
    width: 707px;
    height: 529px;
    background: var(--paper);
    box-shadow: 0 2px 8px rgba(0,0,0,.25);
    overflow: hidden;
  }
  .label--with-botanicals { top: 35px; }
  .label--plain { top: 614px; }

  .swoosh { position: absolute; left: 0; top: 0; width: 707px; height: 529px; }

  .botanicals {
    position: absolute;
    left: 37px; top: 178px;
    width: 290px; height: 200px;
    border-radius: 40% 50% 45% 40%;
    background:
      radial-gradient(ellipse 40% 45% at 72% 62%, rgba(241,154,58,.75), rgba(241,154,58,0) 70%),
      radial-gradient(ellipse 55% 50% at 30% 40%, rgba(139,107,184,.7), rgba(139,107,184,0) 72%);
  }

  .brand-mark { position: absolute; display: flex; flex-direction: column; align-items: center; }
  .brand-mark__dot { border-radius: 50%; border: 4px solid var(--navy); }
  .brand-mark__name { color: var(--navy); letter-spacing: .5px; }

  .front-brand { left: 83px; top: 25px; width: 200px; }
  .front-brand .brand-mark__dot { width: 70px; height: 70px; }
  .front-brand .brand-mark__name { font-size: 23px; margin-top: 38px; }

  .rule { position: absolute; height: 3px; background: linear-gradient(90deg, rgba(201,201,201,0), var(--rule) 20%, var(--rule) 80%, rgba(201,201,201,0)); }
  .front-rule { left: 124px; top: 157px; width: 186px; }

  .skin-types { position: absolute; left: 180px; top: 167px; font-size: 16px; }

  .product-tag {
    position: absolute; left: 70px; top: 381px; width: 245px; height: 26px;
    background: linear-gradient(90deg, var(--teal-deep), var(--teal) 60%, var(--teal-soft));
    font-size: 14px; line-height: 26px; text-align: center; color: #3c3c3c;
    box-shadow: 0 1px 2px rgba(0,0,0,.2);
  }
  .product-tag b { font-family: "Mulish", "Century Gothic", sans-serif; font-weight: 700; }
  .tag-rule { left: 70px; top: 416px; width: 250px; }
  .volume { position: absolute; left: 145px; top: 432px; font-size: 13px; }

  .info-panel {
    position: absolute; left: 365px; top: 32px; width: 311px; height: 416px;
    border: 2px solid #1f1f1f; text-align: center;
  }
  .info-brand { left: 0; top: 22px; width: 100%; }
  .info-brand .brand-mark__dot { width: 44px; height: 44px; border-width: 3px; }
  .info-brand .brand-mark__name { font-size: 14px; margin-top: 8px; }
  .info-panel .rule { left: 59px; width: 190px; }
  .heading { position: absolute; left: 0; width: 100%; font-size: 13px; letter-spacing: .3px; }
  .heading b { font-family: "Mulish", "Century Gothic", sans-serif; font-weight: 700; }
  .copy { position: absolute; left: 0; width: 100%; font-size: 11px; line-height: 13.4px; }

  .footer-rule { position: absolute; left: 0; top: 459px; width: 707px; height: 3px; background: linear-gradient(90deg, rgba(201,201,201,.3), var(--rule) 30%, var(--rule) 70%, rgba(201,201,201,.3)); }
  .claims { position: absolute; left: 30px; top: 478px; font-size: 11px; }
  .claims i { font-style: normal; color: var(--teal-deep); padding: 0 3px; }
  .origin { position: absolute; left: 456px; top: 472px; display: flex; align-items: center; gap: 12px; font-size: 11px; }
  .origin__dot { width: 30px; height: 30px; border-radius: 50%; background: #111; }
</style>
</head>
<body>

<section class="label label--with-botanicals">
  <svg class="swoosh" viewBox="0 0 707 529" aria-hidden="true">
    <defs>
      <linearGradient id="wash-a" x1="0" y1="0" x2="1" y2="1">
        <stop offset="0" stop-color="#bfeaea" stop-opacity=".9"/>
        <stop offset=".6" stop-color="#e9f8f8" stop-opacity=".5"/>
        <stop offset="1" stop-color="#fff" stop-opacity="0"/>
      </linearGradient>
    </defs>
    <path d="M0 138 C120 170 330 240 352 455 L0 455 Z" fill="url(#wash-a)"/>
    <path d="M0 136 C130 165 340 230 356 455 C330 250 120 175 0 150 Z" fill="#8fd9d6"/>
    <path d="M0 136 C130 165 340 230 356 455" fill="none" stroke="#fff" stroke-width="3"/>
  </svg>
  <div class="botanicals" role="img" aria-label="Photograph of lavender sprigs with orange blossoms and a green leaf"></div>

  <div class="brand-mark front-brand"><span class="brand-mark__dot"></span><span class="brand-mark__name">AURELYNE</span></div>
  <div class="rule front-rule"></div>
  <p class="skin-types">For all skin types</p>
  <div class="product-tag"><b>AMINO ACID</b> CLEANSING MOUSSE</div>
  <div class="rule tag-rule"></div>
  <p class="volume">150ml/5 fl.oz</p>

  <div class="info-panel">
    <div class="brand-mark info-brand"><span class="brand-mark__dot"></span><span class="brand-mark__name">AURELYNE</span></div>
    <div class="rule" style="top:112px"></div>
    <p class="heading" style="top:122px"><b>USAGE</b> DIRECTION</p>
    <div class="rule" style="top:141px"></div>
    <p class="copy" style="top:156px">Pump out a small amount onto your palm. Apply onto<br>pre-moistened face and neck and massage for a<br>minute in circular motions to dissolve impurities. Rinse<br>off thoroughly with lukewarm water. Pat dry. Follow<br>with day or night skin care.</p>
    <div class="rule" style="top:246px"></div>
    <p class="heading" style="top:256px"><b>CAUTIONS</b></p>
    <div class="rule" style="top:275px"></div>
    <p class="copy" style="top:293px">Avoid direct contact with eyes. If eye contact occurs,<br>flush thoroughly with water. Consult a physician<br>if irritation persists. Keep out of children’s reach.<br>For external use only.<br><br>Store in a cool, dry place and avoid direct<br>light or heat.</p>
  </div>

  <div class="footer-rule"></div>
  <p class="claims">No sulfates <i>•</i> No synthetic colors <i>•</i> No synthetic fragrance</p>
  <div class="origin"><span class="origin__dot"></span><span>Made in Singapore</span></div>
</section>

<section class="label label--plain">
  <svg class="swoosh" viewBox="0 0 707 529" aria-hidden="true">
    <defs>
      <linearGradient id="wash-b" x1="0" y1="0" x2="1" y2="1">
        <stop offset="0" stop-color="#bfeaea" stop-opacity=".9"/>
        <stop offset=".6" stop-color="#e9f8f8" stop-opacity=".5"/>
        <stop offset="1" stop-color="#fff" stop-opacity="0"/>
      </linearGradient>
    </defs>
    <path d="M0 138 C90 165 150 270 250 280 C320 290 345 360 352 455 L0 455 Z" fill="url(#wash-b)"/>
    <path d="M0 136 C90 160 160 262 255 272 C330 282 352 360 356 455 C345 370 320 298 250 290 C150 280 90 180 0 150 Z" fill="#8fd9d6"/>
    <path d="M0 136 C90 160 160 262 255 272 C330 282 352 360 356 455" fill="none" stroke="#fff" stroke-width="3"/>
  </svg>

  <div class="brand-mark front-brand"><span class="brand-mark__dot"></span><span class="brand-mark__name">AURELYNE</span></div>
  <div class="rule front-rule"></div>
  <p class="skin-types">For all skin types</p>
  <div class="product-tag"><b>AMINO ACID</b> CLEANSING MOUSSE</div>
  <div class="rule tag-rule"></div>
  <p class="volume">150ml/5 fl.oz</p>

  <div class="info-panel">
    <div class="brand-mark info-brand"><span class="brand-mark__dot"></span><span class="brand-mark__name">AURELYNE</span></div>
    <div class="rule" style="top:112px"></div>
    <p class="heading" style="top:122px"><b>USAGE</b> DIRECTION</p>
    <div class="rule" style="top:141px"></div>
    <p class="copy" style="top:156px">Pump out a small amount onto your palm. Apply onto<br>pre-moistened face and neck and massage for a<br>minute in circular motions to dissolve impurities. Rinse<br>off thoroughly with lukewarm water. Pat dry. Follow<br>with day or night skin care.</p>
    <div class="rule" style="top:246px"></div>
    <p class="heading" style="top:256px"><b>CAUTIONS</b></p>
    <div class="rule" style="top:275px"></div>
    <p class="copy" style="top:293px">Avoid direct contact with eyes. If eye contact occurs,<br>flush thoroughly with water. Consult a physician<br>if irritation persists. Keep out of children’s reach.<br>For external use only.<br><br>Store in a cool, dry place and avoid direct<br>light or heat.</p>
  </div>

  <div class="footer-rule"></div>
  <p class="claims">No sulfates <i>•</i> No synthetic colors <i>•</i> No synthetic fragrance</p>
  <div class="origin"><span class="origin__dot"></span><span>Made in Singapore</span></div>
</section>

</body>
</html>
```